Tequila Startup Company Booklet Design

Need a 16 or so page booklet for a spirits company (like tequila) artfully designed. Need a killer design and beautifully and thoughtfully laid out in a compelling manner. Need talented and creative designer to craft an eye catching booklet.
Updates

Low designer entries

Target Market(s)

Investors and tequila drinkers

Industry/Entity Type

Alcohol spirits distillery

Colors

Requirements
Must have
• Beautiful graphics and photos relevant to agave fields
Nice to have
• Want to emphasize the blue agave fields and the distillery process

```html
<!DOCTYPE html>
<html lang="en">
<head>
<meta charset="utf-8">
<title>Our Roots Run Deep — Booklet Spread</title>
<link rel="stylesheet" href="https://fonts.googleapis.com/css2?family=Libre+Baskerville&family=Nunito+Sans:wght@400;500&display=swap">
<style>
  :root {
    --backdrop: #d9d9d9;
    --page: #ececec;
    --ink: #2a2a2a;
    --gold: #bea672;
    --gold-text: #b89a5c;
    --band-text: #fbf8f1;
    --photo-sky: #b9bfb3;
    --photo-agave: #5f7a72;
    --photo-deep: #3e4f48;
    --photo-soil: #6a3a26;
  }
  * { margin: 0; padding: 0; box-sizing: border-box; }
  html, body { width: 1200px; height: 800px; overflow: hidden; background: var(--backdrop); }
  .spread {
    position: absolute; left: 80px; top: 30px;
    width: 1040px; height: 740px;
    display: flex;
    box-shadow: 0 6px 18px rgba(0,0,0,0.12);
  }
  .page { position: relative; width: 520px; height: 740px; background: var(--page); }
  .photo-field {
    width: 100%; height: 100%;
    background:
      linear-gradient(180deg,
        var(--photo-sky) 0%,
        #a7ad9e 16%,
        var(--photo-agave) 30%,
        #6f7f70 52%,
        var(--photo-deep) 70%,
        var(--photo-soil) 86%,
        #3f2c22 100%);
  }
  .page--text { display: flex; flex-direction: column; }
  .content { padding: 32px 48px 0 50px; flex: 1; }
  .title {
    font-family: "Libre Baskerville", Georgia, serif;
    font-weight: 400; font-size: 32px; line-height: 41px;
    letter-spacing: 2.5px; text-transform: uppercase; color: var(--ink);
  }
  .lede {
    margin-top: 50px;
    font-family: "Nunito Sans", Arial, sans-serif;
    font-size: 17.5px; line-height: 23px; color: var(--gold-text);
  }
  .body-copy {
    margin-top: 40px;
    font-family: "Nunito Sans", Arial, sans-serif;
    font-size: 14.5px; line-height: 22px; color: var(--ink);
  }
  .body-copy p + p { margin-top: 22px; }
  .closing-band {
    height: 128px; background: var(--gold);
    display: flex; align-items: center; justify-content: center;
    text-align: center;
    font-family: "Nunito Sans", Arial, sans-serif;
    font-size: 17.5px; line-height: 24px; color: var(--band-text);
    padding: 0 30px;
  }
</style>
</head>
<body>
  <main class="spread">
    <section class="page page--photo">
      <div class="photo-field" role="img" aria-label="Photograph of a jimador in a straw hat harvesting blue agave with a coa in a field of red volcanic soil"></div>
    </section>
    <section class="page page--text">
      <div class="content">
        <h1 class="title">Our Roots<br>Run Deep</h1>
        <p class="lede">Our foundation is built on more than land<br>— it’s built on legacy.</p>
        <div class="body-copy">
          <p>In the Highlands of Jalisco, where elevation, climate, and volcanic soil converge, we cultivate 100% Blue Weber Agave with time-honored methods passed down through generations of skilled jimadores. This region isn’t just where our agave grows — it’s where our identity was born.</p>
          <p>We are rooted in tradition but driven by opportunity. With a deep respect for the craft, we fuse artisanal production with modern precision to create a tequila of uncompromising quality. The result: a premium spirit that reflects provenance, integrity, and cultural authenticity.</p>
          <p>As we launch into new markets, our commitment remains grounded — to the land, to our partners, and to producing tequila that stands apart in a growing global category.</p>
        </div>
      </div>
      <div class="closing-band">
        <p>This is not just a product. It’s a long-term<br>investment in story, place, and sustainable growth.</p>
      </div>
    </section>
  </main>
</body>
</html>
```